Tolvern Business Cards

Business card design. dont mind if new logo is suggested.
it would be for a security company.
our clients would be bigger security companies around Australia.
have a logo done but can be replaced. see attaached. like the colors.
Need company name, person name, designation, phone and email on front.
At back company logo and name. website saddress and 2 x license numbers
would like to have 2 different background color for both sidde

Industry/Entity Type

Security

Contact Information for Business Card

round corners, front should be light in color. need logo at back with webaddress and 2 x license numners

Font styles to use
Sans Serif

Colors
f37122
faa54b
f8ba93
0255a3
0592cd
85cae6
b3d448
9bcb3c
ffffff

Requirements
Must have
• see description
Nice to have
• see description
Should not have
• should not be difficult to read or hardd to find information on card.. lets say easy on eyes yet catchy

```html
<!DOCTYPE html>
<html lang="en">
<head>
<meta charset="utf-8">
<title>Tolvern Business Cards</title>
<link rel="stylesheet" href="https://fonts.googleapis.com/css2?family=Roboto+Condensed:wght@400;700&family=Open+Sans:wght@400;600&display=swap">
<style>
  :root {
    --stage: #3b2a21;
    --card-light: #f7f9fb;
    --ink-grey: #5a5a5a;
    --ink-soft: #777a7e;
    --bubble: #e4e6e9;
    --navy: #1d3563;
    --navy-strip: #20427a;
    --navy-edge: #2a4e86;
    --cyan: #0aa5cc;
    --white: #ffffff;
  }
  * { margin: 0; padding: 0; box-sizing: border-box; }
  html, body { width: 1200px; height: 1000px; overflow: hidden; }
  body {
    background: var(--stage);
    position: relative;
    font-family: "Roboto Condensed", "Arial Narrow", sans-serif;
  }
  .card {
    position: absolute;
    width: 440px;
    height: 250px;
    border-radius: 16px;
    overflow: hidden;
    box-shadow: 0 6px 18px rgba(0,0,0,.45);
  }

  /* Front */
  .card-front { left: 170px; top: 220px; background: var(--card-light); }
  .front-pattern {
    position: absolute; right: 0; top: 0; width: 300px; height: 210px;
    background: radial-gradient(ellipse at 55% 45%, var(--bubble) 0%, rgba(228,230,233,.45) 45%, rgba(247,249,251,0) 75%);
  }
  .front-brand { position: absolute; left: 40px; top: 112px; color: var(--ink-grey); }
  .front-brand .brand-name { font-size: 46px; font-weight: 700; line-height: 1; letter-spacing: .5px; }
  .front-brand .brand-sub { font-size: 19px; font-weight: 700; line-height: 1.1; letter-spacing: .5px; }
  .front-divider { position: absolute; left: 222px; top: 78px; width: 1px; height: 92px; background: #8c8f93; }
  .contact { position: absolute; left: 240px; top: 74px; color: var(--ink-grey); }
  .contact .person { font-size: 23px; font-weight: 700; line-height: 1.05; }
  .contact .role { font-size: 17px; line-height: 1.1; margin-bottom: 8px; }
  .contact .line { font-size: 16px; line-height: 1.25; color: var(--ink-soft); }
  .front-band-cyan { position: absolute; left: 0; bottom: 0; width: 100%; height: 12px; background: var(--cyan); }
  .front-band-navy { position: absolute; left: 250px; bottom: 0; width: 190px; height: 40px; background: var(--navy); }

  /* Back */
  .card-back { left: 590px; top: 520px; background: var(--navy); }
  .back-mark {
    position: absolute; left: 46px; top: 52px; width: 100px; height: 100px;
    border-radius: 50%; background: var(--white);
  }
  .back-brand { position: absolute; left: 170px; top: 58px; color: var(--white); font-weight: 700; }
  .back-brand .brand-name { font-size: 52px; line-height: 1; letter-spacing: 1px; }
  .back-brand .brand-sub { font-size: 24px; line-height: 1.1; letter-spacing: .5px; }
  .back-strip {
    position: absolute; left: 0; bottom: 18px; width: 100%; height: 28px;
    background: var(--navy-strip);
    border-top: 2px solid var(--navy-edge); border-bottom: 2px solid var(--navy-edge);
    display: flex; justify-content: space-between; align-items: center;
    padding: 0 22px;
    font-family: "Open Sans", Arial, sans-serif; font-size: 11px; color: var(--white); letter-spacing: .4px;
  }
</style>
</head>
<body>
  <section class="card card-front" aria-label="Business card front">
    <div class="front-pattern" role="img" aria-label="Soft pattern of pale grey dots"></div>
    <div class="front-brand">
      <div class="brand-name">TOLVERN</div>
      <div class="brand-sub">SECURITY GROUP</div>
    </div>
    <div class="front-divider"></div>
    <div class="contact">
      <div class="person">ALEX REED</div>
      <div class="role">manager</div>
      <div class="line">019 482 7730</div>
      <div class="line">alex@tolvern.example</div>
    </div>
    <div class="front-band-cyan"></div>
    <div class="front-band-navy"></div>
  </section>

  <section class="card card-back" aria-label="Business card back">
    <div class="back-mark"></div>
    <div class="back-brand">
      <div class="brand-name">TOLVERN</div>
      <div class="brand-sub">SECURITY GROUP</div>
    </div>
    <div class="back-strip">
      <span class="licence">LICENCE NO: #48213, #57106</span>
      <span class="website">www.TolvernSecurityGroup.com</span>
    </div>
  </section>
</body>
</html>
```